Transparent Real Estate Experience

Looking for an Image/Graphic for a postcard and brochure that communicates a complete transparent experience when selling a home.
The image is to convey "seeing through", hence transparent or transparency. NO Hourglasses or magnifying glasses. To me, those convey different messages - hour glass is "time" and magnifying is "making something small look bigger".

Ideally, a glass house with the words under the glass so the house is transparent to the words that are being communicated.

Those are:
transparency, honesty, communication, integrity, ethics, clarity, principles, knowledge, experience, trust, fairness, responsibility.

OR - using a "glass font" with those words in a mosaic order so the words are all transparent.

Professional Look - no cartoons...See samples - only thing I could find to provide a starting point. Thanks!
Updates

Target Market(s)

People selling their homes

Industry/Entity Type

Real Estate

Colors
0054AA
0677BA
7BADD7
CADEEF
E8F1F8

Requirements
Must have
• "Transparent" Look - "See-through"
Should not have
• Cartoons

```html
<!DOCTYPE html>
<html lang="en">
<head>
<meta charset="utf-8">
<title>Transparent Real Estate Experience</title>
<link rel="stylesheet" href="https://fonts.googleapis.com/css2?family=Oswald:wght@600&family=Indie+Flower&display=swap">
<style>
  :root {
    --bg-deep: #4a4690;
    --bg-mid: #6d69b0;
    --bg-light: #8c89c4;
    --glass: rgba(240, 240, 250, 0.82);
    --glass-soft: rgba(225, 225, 245, 0.45);
    --edge: #5b4fa0;
    --word: #4c3f98;
    --word-halo: #ffffff;
    --caption: #ffffff;
    --lawn-top: #2f7d1f;
    --lawn-bottom: #1d5a12;
  }
  html, body {
    margin: 0;
    padding: 0;
    overflow: hidden;
  }
  .canvas {
    position: relative;
    width: 1200px;
    height: 1200px;
    overflow: hidden;
    background: linear-gradient(180deg, var(--bg-deep) 0%, var(--bg-mid) 55%, var(--bg-light) 100%);
  }
  .artwork {
    position: absolute;
    inset: 0;
    width: 1200px;
    height: 1200px;
  }
  .value-word {
    font-family: "Oswald", "Arial Narrow", sans-serif;
    font-weight: 600;
    font-size: 70px;
    fill: var(--word);
    stroke: var(--word-halo);
    stroke-width: 5px;
    paint-order: stroke;
    text-anchor: middle;
    dominant-baseline: central;
  }
  .caption {
    position: absolute;
    left: 72px;
    top: 874px;
    width: 490px;
    margin: 0;
    font-family: "Indie Flower", cursive;
    font-size: 47px;
    line-height: 54px;
    color: var(--caption);
  }
</style>
</head>
<body>
<main class="canvas">
  <svg class="artwork" viewBox="0 0 1500 1500" xmlns="http://www.w3.org/2000/svg">
    <defs>
      <linearGradient id="sceneTone" x1="0" y1="0" x2="0" y2="1">
        <stop offset="0" stop-color="#8fd0e0"/>
        <stop offset="1" stop-color="#6f9e7a"/>
      </linearGradient>
      <linearGradient id="homeTone" x1="0" y1="0" x2="0" y2="1">
        <stop offset="0" stop-color="#4e5a66"/>
        <stop offset="0.35" stop-color="#e9ddc6"/>
        <stop offset="1" stop-color="#c9b89a"/>
      </linearGradient>
      <linearGradient id="lawnTone" x1="0" y1="0" x2="0" y2="1">
        <stop offset="0" stop-color="var(--lawn-top)"/>
        <stop offset="1" stop-color="var(--lawn-bottom)"/>
      </linearGradient>
    </defs>

    <rect class="aerial-backdrop" x="0" y="0" width="1500" height="1430" fill="#5a56a0" opacity="0.35" role="img" aria-label="Faded aerial view of a residential neighbourhood"/>

    <g class="glass-hexagon">
      <polygon points="450,52 1020,52 1300,543 1020,1030 450,1030 170,543" fill="var(--glass)" stroke="var(--edge)" stroke-width="3"/>
      <polygon class="house-view" points="568,230 900,230 1100,543 900,843 568,843 368,543" fill="url(#sceneTone)" opacity="0.8" role="img" aria-label="Photo of a two-storey white house seen from above through glass"/>
      <polygon points="568,230 900,230 1100,543 900,843 568,843 368,543" fill="var(--glass-soft)" stroke="var(--edge)" stroke-width="3"/>
      <g fill="none" stroke="var(--edge)" stroke-width="2.5">
        <polyline points="368,543 900,230 905,843 368,543"/>
        <polyline points="568,230 1100,543 568,843 568,230"/>
        <line x1="450" y1="52" x2="900" y2="230"/>
        <line x1="450" y1="52" x2="368" y2="543"/>
        <line x1="1020" y1="52" x2="568" y2="230"/>
        <line x1="1020" y1="52" x2="1100" y2="543"/>
        <line x1="1300" y1="543" x2="900" y2="230"/>
        <line x1="1300" y1="543" x2="905" y2="843"/>
        <line x1="1020" y1="1030" x2="1100" y2="543"/>
        <line x1="1020" y1="1030" x2="568" y2="843"/>
        <line x1="450" y1="1030" x2="905" y2="843"/>
        <line x1="450" y1="1030" x2="368" y2="543"/>
        <line x1="170" y1="543" x2="568" y2="843"/>
        <line x1="170" y1="543" x2="568" y2="230"/>
        <line x1="170" y1="543" x2="368" y2="543"/>
      </g>
    </g>

    <g class="value-words">
      <text class="value-word" textLength="130" lengthAdjust="spacingAndGlyphs" transform="translate(780 97)">TRUST</text>
      <text class="value-word" textLength="215" lengthAdjust="spacingAndGlyphs" transform="translate(575 150) rotate(29)">FAIRNESS</text>
      <text class="value-word" textLength="285" lengthAdjust="spacingAndGlyphs" transform="translate(1052 292) rotate(40)">KNOWLEDGE</text>
      <text class="value-word" textLength="265" lengthAdjust="spacingAndGlyphs" transform="translate(305 405) rotate(-56)">EXPERIENCE</text>
      <text class="value-word" textLength="345" lengthAdjust="spacingAndGlyphs" transform="translate(612 328) rotate(-35)">RESPONSIBILITY</text>
      <text class="value-word" textLength="358" lengthAdjust="spacingAndGlyphs" transform="translate(948 535) rotate(-90)">COMMUNICATION</text>
      <text class="value-word" textLength="348" lengthAdjust="spacingAndGlyphs" transform="translate(665 648) rotate(32)">TRANSPARENCY</text>
      <text class="value-word" textLength="222" lengthAdjust="spacingAndGlyphs" transform="translate(1120 625) rotate(-41)">HONESTY</text>
      <text class="value-word" textLength="262" lengthAdjust="spacingAndGlyphs" transform="translate(308 680) rotate(56)">PRINCIPLES</text>
      <text class="value-word" textLength="172" lengthAdjust="spacingAndGlyphs" transform="translate(1073 828) rotate(-50)">ETHICS</text>
      <text class="value-word" textLength="230" lengthAdjust="spacingAndGlyphs" transform="translate(658 884) rotate(-32)">INTEGRITY</text>
      <text class="value-word" textLength="167" lengthAdjust="spacingAndGlyphs" transform="translate(798 985)">CLARITY</text>
    </g>

    <rect class="lawn" x="0" y="1426" width="1500" height="74" fill="url(#lawnTone)"/>
    <polygon class="home-photo" points="720,1140 790,1060 1100,1060 1200,1030 1500,1030 1500,1440 720,1440" fill="url(#homeTone)" role="img" aria-label="Photo of a single-storey home with lit porch, garden and a family standing by the front door"/>
  </svg>

  <p class="caption">We make your dream home come true in a homestay and transparent way!!!</p>
</main>
</body>
</html>
```